Ridgewell Stonecraft Construction Needs business card

Hey we are in need of business card designs. I have upload our logo as a guideline, but free feel to run with it or come up with something unique.
Pls have fun with it and be creative. the name says it all!
i will give some directions after i see a few entries..
Logo source file has been uploaded..
Hey because of the logo is so colourful already.
Can we have a few submissions with less colour.
Also we are looking for clever/hidden/descriptive business card.

```html
<!DOCTYPE html>
<html lang="en">
<head>
<meta charset="utf-8">
<title>Ridgewell Stonecraft Construction – Business Card</title>
<link rel="stylesheet" href="https://fonts.googleapis.com/css2?family=Arimo:wght@400;700&display=swap">
<style>
  :root {
    --stage: #b9b9b9;
    --card: #ffffff;
    --band: #a7a7a7;
    --ink: #1d1d1d;
    --brand-grey: #6e6e6e;
    --accent-red: #e8231c;
    --brick-red: #e41e26;
    --brick-green: #13a54a;
    --brick-blue: #1677c8;
    --brick-black: #222222;
  }
  * { box-sizing: border-box; margin: 0; padding: 0; }
  html, body {
    width: 1200px; height: 960px; overflow: hidden;
    background: var(--stage);
    font-family: "Arimo", Arial, sans-serif;
  }
  .canvas { position: relative; width: 1200px; height: 960px; }

  .card {
    position: absolute;
    width: 620px; height: 355px;
    background: var(--card);
    box-shadow: 0 6px 18px rgba(0,0,0,.25);
    overflow: hidden;
  }
  .card--back { left: 70px; top: 80px; }
  .card--front { left: 510px; top: 500px; }

  .brick-strip {
    position: absolute; left: 0; right: 0; bottom: 18px; height: 40px;
    background: linear-gradient(90deg,
      var(--brick-black), var(--brick-blue) 25%, var(--brick-red) 50%,
      var(--brick-green) 75%, var(--brick-black));
    opacity: .85;
  }

  /* back side */
  .contact-band {
    position: absolute; left: 0; right: 0; top: 70px; height: 190px;
    background: var(--band);
  }
  .person-name {
    position: absolute; left: 20px; top: 118px;
    color: var(--accent-red); font-size: 14px; font-variant: small-caps;
    letter-spacing: .5px;
  }
  .icon-rail {
    position: absolute; left: 20px; top: 158px; width: 16px; height: 92px;
    background: var(--accent-red);
  }
  .contact-list {
    position: absolute; left: 50px; top: 156px; list-style: none;
    color: var(--ink); font-size: 13px; line-height: 23px;
  }
  .brand-lockup--small {
    position: absolute; right: 26px; top: 150px; text-align: center;
    color: var(--brand-grey); font-weight: 700;
  }
  .brand-lockup--small .brand-name { font-size: 26px; letter-spacing: -.5px; }
  .brand-lockup--small .brand-sub { font-size: 12px; letter-spacing: 1px; }
  .address {
    position: absolute; right: 26px; top: 272px;
    font-size: 12px; font-weight: 700; color: var(--ink);
  }

  /* front side */
  .brand-lockup--large {
    position: absolute; left: 0; right: 0; top: 100px; text-align: center;
    color: var(--brand-grey); font-weight: 700;
  }
  .brand-mark {
    display: inline-block; width: 46px; height: 46px;
    background: var(--brand-grey); margin-bottom: 18px;
  }
  .brand-lockup--large .brand-name { font-size: 44px; letter-spacing: -1px; line-height: 1.05; }
  .brand-lockup--large .brand-sub { font-size: 20px; letter-spacing: 2px; margin-top: 4px; }
</style>
</head>
<body>
<main class="canvas">

  <section class="card card--back" aria-label="Business card, contact side">
    <div class="contact-band"></div>
    <p class="person-name">Name Surname</p>
    <svg class="icon-rail" viewBox="0 0 16 92" aria-hidden="true">
      <rect x="4" y="4" width="8" height="13" rx="1.5" fill="#13a54a"/>
      <rect x="3" y="29" width="10" height="9" fill="#13a54a"/>
      <rect x="3" y="52" width="10" height="8" fill="#13a54a"/>
      <polyline points="3,52 8,57 13,52" fill="none" stroke="#e8231c" stroke-width="1"/>
      <circle cx="8" cy="78" r="5" fill="#f2b01e"/>
    </svg>
    <ul class="contact-list">
      <li>55 555 55555</li>
      <li>44 4444 4444</li>
      <li>info@ridgewellstonecraft.com</li>
      <li>www.ridgewellstonecraft.com</li>
    </ul>
    <div class="brand-lockup--small">
      <p class="brand-name">RIDGEWELL STONECRAFT</p>
      <p class="brand-sub">CONSTRUCTION</p>
    </div>
    <p class="address">Door no, state, zipcode,Country</p>
    <div class="brick-strip" role="img" aria-label="Decorative band of coloured bricks"></div>
  </section>

  <section class="card card--front" aria-label="Business card, brand side">
    <div class="brand-lockup--large">
      <span class="brand-mark" aria-hidden="true"></span>
      <p class="brand-name">RIDGEWELL STONECRAFT</p>
      <p class="brand-sub">CONSTRUCTION</p>
    </div>
    <div class="brick-strip" role="img" aria-label="Decorative band of coloured bricks"></div>
  </section>

</main>
</body>
</html>
```